Tirovel

We need a business card for our company is a holding for different business all are different we try to have some air of relax and fun in our projects we add pictures of the office to give you an idea od the mood of the business

Business

```html
<!DOCTYPE html>
<html lang="en">
<head>
<meta charset="utf-8">
<title>Tirovel — Business Card</title>
<link rel="stylesheet" href="https://fonts.googleapis.com/css2?family=Montserrat:wght@500;600;800&display=swap">
<style>
  :root {
    --stage: #2b2b2d;
    --brown: #5e3a12;
    --yellow: #f7e531;
    --charcoal: #2f2e2f;
    --white: #ffffff;
    --ink: #1e1e1e;
    --rule: #a88a6a;
  }
  * { box-sizing: border-box; margin: 0; padding: 0; }
  html, body {
    width: 1200px;
    height: 800px;
    overflow: hidden;
    background: var(--stage);
    font-family: "Montserrat", sans-serif;
  }
  .stage {
    position: relative;
    width: 1200px;
    height: 800px;
  }
  .card {
    position: absolute;
    top: 100px;
    width: 340px;
    height: 595px;
    border-radius: 28px;
    overflow: hidden;
  }

  /* Front: brand side */
  .card-front {
    left: 200px;
    background: var(--brown);
    display: flex;
    flex-direction: column;
    align-items: center;
    padding-top: 170px;
  }
  .brand-lockup {
    display: flex;
    align-items: center;
    gap: 14px;
  }
  .brand-square {
    width: 34px;
    height: 34px;
    background: var(--yellow);
  }
  .brand-name {
    font-weight: 800;
    font-size: 52px;
    color: var(--yellow);
    letter-spacing: -1px;
    line-height: 1;
  }
  .front-rule {
    width: 272px;
    height: 1px;
    background: var(--rule);
    margin-top: 96px;
  }
  .front-web {
    margin-top: 16px;
    font-weight: 600;
    font-size: 15px;
    letter-spacing: 3px;
    color: var(--yellow);
  }

  /* Back: contact side */
  .card-back {
    left: 660px;
    background: var(--white);
  }
  .back-head {
    height: 300px;
    background: var(--charcoal);
    display: flex;
    align-items: flex-end;
    padding: 0 0 34px 30px;
  }
  .back-brand {
    font-weight: 800;
    font-size: 64px;
    color: var(--white);
    letter-spacing: -2px;
    line-height: 1;
  }
  .name-band {
    margin-top: 14px;
    height: 58px;
    background: var(--charcoal);
    display: flex;
    align-items: center;
    padding-left: 30px;
  }
  .person-name {
    font-weight: 600;
    font-size: 22px;
    letter-spacing: 2.5px;
    color: var(--yellow);
  }
  .contact-list {
    list-style: none;
    padding: 44px 0 0 30px;
  }
  .contact-list li {
    font-weight: 600;
    font-size: 19px;
    color: var(--ink);
    line-height: 1.55;
  }
</style>
</head>
<body>
  <main class="stage">
    <section class="card card-front" aria-label="Card front">
      <div class="brand-lockup">
        <span class="brand-square" aria-hidden="true"></span>
        <span class="brand-name">Tirovel</span>
      </div>
      <div class="front-rule"></div>
      <p class="front-web">WWW.TIROVEL.COM</p>
    </section>

    <section class="card card-back" aria-label="Card back">
      <div class="back-head">
        <span class="back-brand">Tirovel</span>
      </div>
      <div class="name-band">
        <p class="person-name">MARISOL VEGA</p>
      </div>
      <ul class="contact-list">
        <li>555.014.2290</li>
        <li>marisol@tirovel.com</li>
        <li>www.tirovel.com</li>
      </ul>
    </section>
  </main>
</body>
</html>
```